Business card design needed

Looking for an innovative design that portrays a professional image for our company. We are a structural steel erection, EWP and crane hire company. We are looking at having business and contact details on front of card and perhaps a list of what we hire on the back of the card. Our company machine colours are royal blue and silver at present but would be open to change with our cards...
Updates
We are looking for double sided designs due to the amount of information required on the card
The Logo uploaded if the logo we have been using, however our company name has changed to just "Steady Summit Lifting". I have uploaded the image just for ideas...
Reason: Allowing more time for more design submissions
Reason: Want more dedigns
Target Market(s)
Construction/Industrial
Industry/Entity Type
Structural Steel
Contact Information for Business Card
Business Name: Steady Summit Lifting
Specialising in Structural Steel Erection, Equipment & Crane Hire
Address: 27 Corwin Street, Balmoral Q 4571
Site Contact: Dale Morven - 0431 597 203 - dale@sslifting.example
Office Contact: Lina Fairbrook - 0419 735 214 - lina@sslifting.example
We hire Forklifts, Telehandlers, Scissor-lifts, Boom-lifts, 3T Mini Cranes, 16T/20T Bexlo, Prime mover with extendable trailer (13.5-22m), Qualified Boilermakers,Riggers and Dogman.
Logo Text
Steady Summit Lifting or SSL
Logo styles of interest
Emblem Logo
Look and feel

```html
<!DOCTYPE html>
<html lang="en">
<head>
<meta charset="utf-8">
<title>Steady Summit Lifting – Business Card Back</title>
<link href="https://fonts.googleapis.com/css2?family=Roboto+Condensed:wght@300;700&display=swap" rel="stylesheet">
<style>
  :root {
    --royal-blue: #4f6ff2;
    --band-blue: #4d6ef0;
    --charcoal: #262626;
    --steel-grey: #59626a;
    --silver: #d2d5d5;
    --silver-deep: #c3c8c8;
    --sky: #9fc3e6;
    --site-grey: #8e959a;
  }
  * { margin: 0; padding: 0; box-sizing: border-box; }
  html, body { width: 1200px; height: 741px; overflow: hidden; background: #fff; }
  .card {
    position: relative; width: 1200px; height: 741px; overflow: hidden;
    font-family: "Roboto Condensed", "Arial Narrow", sans-serif;
    background: var(--silver);
  }
  .photo-strip { position: absolute; top: 0; left: 0; width: 1200px; height: 128px; display: flex; }
  .photo-strip .site-photo { flex: 1; height: 100%; border-right: 2px solid #fff; }
  .site-photo:nth-child(odd) { background: linear-gradient(180deg, var(--sky) 0%, #c9d6df 55%, var(--site-grey) 100%); }
  .site-photo:nth-child(even) { background: linear-gradient(180deg, #b7cde2 0%, #a8adb0 50%, #7d8589 100%); }
  .site-photo:last-child { border-right: none; }
  .band-blue { position: absolute; left: 0; width: 1200px; background: var(--band-blue); }
  .band-blue.upper { top: 128px; height: 18px; }
  .band-blue.lower { top: 303px; height: 21px; }
  .name-panel {
    position: absolute; top: 146px; left: 0; width: 1200px; height: 157px;
    background: var(--charcoal);
    display: flex; align-items: center; justify-content: center;
  }
  .brand-name {
    color: var(--royal-blue); font-weight: 300; font-size: 96px;
    letter-spacing: 3px; line-height: 1;
  }
  .steel-backdrop {
    position: absolute; top: 324px; left: 0; width: 1200px; height: 417px;
    background: linear-gradient(135deg, var(--silver) 0%, var(--silver-deep) 50%, var(--silver) 100%);
  }
  .tagline {
    position: absolute; top: 338px; left: 0; width: 1200px; text-align: center;
    color: var(--steel-grey); font-weight: 700; font-size: 56px; letter-spacing: 0.5px;
  }
  .hire-heading {
    position: absolute; top: 474px; left: 75px;
    color: var(--royal-blue); font-weight: 700; font-size: 40px;
  }
  .hire-list { position: absolute; top: 522px; left: 108px; list-style: none; }
  .hire-list li {
    color: var(--steel-grey); font-weight: 700; font-size: 31px; line-height: 43.5px;
    white-space: nowrap;
  }
  .hire-list .dot { color: var(--royal-blue); margin: 0 6px; }
  .hire-list .dot.lead { margin: 0 18px 0 0; }
</style>
</head>
<body>
<div class="card">
  <div class="photo-strip">
    <div class="site-photo" role="img" aria-label="Steel frame under construction with workers on site"></div>
    <div class="site-photo" role="img" aria-label="Concrete wall panel with elevated work platform"></div>
    <div class="site-photo" role="img" aria-label="Blue crane lifting steel at a building site"></div>
    <div class="site-photo" role="img" aria-label="Prime mover with container on trailer"></div>
    <div class="site-photo" role="img" aria-label="Steel beams laid out with tower crane behind"></div>
    <div class="site-photo" role="img" aria-label="Mini crane placing a beam against a concrete wall"></div>
    <div class="site-photo" role="img" aria-label="Completed steel portal frame with lift"></div>
  </div>
  <div class="band-blue upper"></div>
  <div class="name-panel">
    <span class="brand-name">Steady Summit Lifting</span>
  </div>
  <div class="band-blue lower"></div>
  <div class="steel-backdrop" role="img" aria-label="Faint structural steel lattice background"></div>
  <h1 class="tagline">Specialising in Structural Steel Erection</h1>
  <h2 class="hire-heading">We hire</h2>
  <ul class="hire-list">
    <li><span class="dot lead">•</span>Forklifts <span class="dot">•</span> Telehandlers <span class="dot">•</span> Scissor-lifts <span class="dot">•</span> Boom-lifts <span class="dot">•</span> T Mini Cranes</li>
    <li><span class="dot lead">•</span>16T/20T Bexlo <span class="dot">•</span> Prime mover with extendable trailer (13.5-22m)</li>
    <li><span class="dot lead">•</span>Qualified Boilermakers,Riggers and Dogman</li>
  </ul>
</div>
</body>
</html>
```